Vocational Mentor needs an impressive business card

1. I need a business card (or maybe three with identic look) to promote me and my three business titles/services:
- Vocational Mentor. I help people find their vocation and live happily from it. I use my 20 years of experience in business, management and psychology to help them identify the most efficient ways to make a living doing what they are passionate about.
- Business Angel. I help founders start a succesful business with minimum risks and costs. I use my 20 years of experience in sales, management and entrepreneurship to help them identify the most efficient ways, in terms of time and cost, to validate their business idea.
- Learning Designer. I design unique learning programs that produce long-term cognitive and behavioural changes to people and organisations. I use my 20 years of experience in learning, teaching and change management to create minimalist experiences and processes that allow them to change efficiently in their pursued direction.

2. I would like a two-sided business card, on the front with my name, contact details and titles, on the back the explanation of the services.
Updates

Hi all,

I updated my brief, included contacts info and give feedback on all designs I got. I am new on this platform so please tell me if you need anything else or if I don't use corectly the platform forms.

Kind regards,
Tudor

Hi all,

I shortened the services description by deleting the phrase "I call..."

Kind regards,
Tudor

Target Market(s)

Freelancers, startups, people and organization willing to invest in change through ultimate learning experiences

Industry/Entity Type

Business

Font styles to use
Serif

Requirements
Must have
• Front side: full name, titles, web site, email, phone like below:
Tudor Vasilache
Vocational Mentor, Business Angel, Learning Designer
info@tudorvasilache.example
www.tudorvasilache.example
+40-745-TUDORV
Nice to have
• Back side: the description of the services I provide as in the task description.
1/3: it would be nice if I can jam all three titles on the front side but then I need a solution to jam all three services on the back side.

```html
<!DOCTYPE html>
<html lang="en">
<head>
<meta charset="utf-8">
<title>Tudor Vasilache – Business Card</title>
<link rel="stylesheet" href="https://fonts.googleapis.com/css2?family=Arimo:wght@400;700&display=swap">
<style>
  :root {
    --card: #272526;
    --paper: #ffffff;
    --accent: #4b6b2b;
    --ink: #ffffff;
  }
  * { margin: 0; padding: 0; box-sizing: border-box; }
  html, body {
    width: 933px;
    height: 1200px;
    overflow: hidden;
    background: var(--paper);
    font-family: "Arimo", Arial, sans-serif;
    color: var(--ink);
  }
  .canvas { position: relative; width: 933px; height: 1200px; }
  .card {
    position: absolute;
    left: 0;
    width: 933px;
    background: var(--card);
    overflow: hidden;
  }
  .card--front { top: 0; height: 564px; }
  .card--back { top: 635px; height: 565px; }
  .bar { position: absolute; background: var(--accent); }

  .name {
    position: absolute;
    left: 148px;
    top: 68px;
    font-size: 55px;
    font-weight: 700;
    line-height: 1;
    white-space: nowrap;
  }
  .titles {
    position: absolute;
    left: 148px;
    top: 145px;
    font-size: 27px;
    line-height: 1;
    white-space: nowrap;
  }
  .contact {
    position: absolute;
    font-size: 27px;
    line-height: 1;
    white-space: nowrap;
  }
  .contact--web { left: 52px; top: 461px; }
  .contact--mail { left: 440px; top: 461px; }
  .contact--phone { left: 308px; top: 510px; }

  .service {
    position: absolute;
    left: 30px;
    width: 855px;
    font-size: 22.5px;
    line-height: 27.6px;
  }
  .service span { display: block; white-space: nowrap; }
  .service--justified span { text-align: justify; text-align-last: justify; }
  .service--justified span:last-child { text-align-last: left; }
  .service--mentor { top: 60px; }
  .service--angel { top: 227px; }
  .service--design { top: 374px; }
</style>
</head>
<body>
<main class="canvas">
  <section class="card card--front" aria-label="Front side">
    <div class="bar" style="left:72px; top:0; width:10px; height:247px;"></div>
    <div class="bar" style="left:93px; top:0; width:11px; height:247px;"></div>
    <div class="bar" style="left:851px; top:456px; width:82px; height:9px;"></div>
    <div class="bar" style="left:851px; top:477px; width:82px; height:11px;"></div>

    <h1 class="name">Tudor Vasilache</h1>
    <p class="titles">Vocational Mentor, Business Angel, Learning Designer</p>
    <p class="contact contact--web">www.tudorvasilache.example</p>
    <p class="contact contact--mail">info@tudorvasilache.example</p>
    <p class="contact contact--phone">+40-745-TUDORV</p>
  </section>

  <section class="card card--back" aria-label="Back side">
    <div class="bar" style="left:896px; top:0; width:7px; height:565px;"></div>
    <div class="bar" style="left:907px; top:0; width:7px; height:565px;"></div>
    <div class="bar" style="left:0; top:524px; width:82px; height:5px;"></div>
    <div class="bar" style="left:0; top:535px; width:82px; height:5px;"></div>

    <p class="service service--mentor">
      <span>- Vocational Mentor. I help people to find their vocation and live happily from it.</span>
      <span>I use my 20 years of experience in business, management and psychology to</span>
      <span>help them identify the most efficient ways to make a living doing what they are</span>
      <span>passionate about.</span>
    </p>
    <p class="service service--angel">
      <span>- Business Angel. I help founders to start a succesful business with minimum</span>
      <span>risks and costs. I use my 20 years of experience in sales, management and</span>
      <span>entrepreneurship to help them identify the most efficient ways, in terms of time</span>
      <span>and cost, to validate their business idea.</span>
    </p>
    <p class="service service--design service--justified">
      <span>- Learning Designer. I design unique learning programs that produce long-term</span>
      <span>cognitive and behavioural changes to people and organisations. I use my 20</span>
      <span>years of experience in learning, teaching and change management to create</span>
      <span>minimalist experiences and processes that allows them to change efficiently in</span>
      <span>their pursued direction.</span>
    </p>
  </section>
</main>
</body>
</html>
```